New Business Cards for KM&DR

We need updated business cards for a staff of 15 engineers, estimators, project managers, and sales people. We have recently begun changes to our website and marketing material to improve our look and branding. We are an established fabricator specializing in pressure vessels, tanks, and structural steel. The owners require us to use the existing logo and old english text design. Also, we prefer dark grey or mostly black cards.
Target Market(s)
Engineers, purchasing agents, estimators, and project managers of; mining companies, refineries, industrial construction professionals
Industry/Entity Type
Business
Contact Information for Business Card
Logo, phone, website, email, etc.
Look and feel
Each slider illustrates characteristics of the customer's brand and the style your logo design should communicate.

```html
<!DOCTYPE html>
<html lang="en">
<head>
<meta charset="utf-8">
<title>KM&amp;DR Business Cards</title>
<link href="https://fonts.googleapis.com/css2?family=Open+Sans:wght@400;600;700&display=swap" rel="stylesheet">
<style>
  :root {
    --backdrop: #3b3432;
    --card-black: #141414;
    --card-edge: #0b0b0b;
    --ink-white: #ffffff;
    --ink-soft: #d9d9d9;
    --ink-muted: #8c8c8c;
    --foil: #5a5a5a;
  }
  * { box-sizing: border-box; margin: 0; padding: 0; }
  html, body {
    width: 1200px; height: 864px; overflow: hidden;
    background: var(--backdrop);
    font-family: "Open Sans", Arial, sans-serif;
  }
  .canvas { position: relative; width: 1200px; height: 864px; }

  .card {
    position: absolute;
    width: 525px; height: 300px;
    background: linear-gradient(160deg, #1b1b1b 0%, var(--card-black) 60%, #0f0f0f 100%);
    border: 1px solid var(--card-edge);
    border-radius: 4px;
    box-shadow: 0 14px 30px rgba(0,0,0,.45);
  }
  .card-front { left: 55px; top: 90px; }
  .card-back  { left: 620px; top: 440px; }

  /* front */
  .front-mark {
    position: absolute; left: 0; right: 0; top: 92px;
    display: flex; align-items: center; justify-content: center; gap: 14px;
  }
  .front-mark .mark-square {
    width: 22px; height: 22px; background: var(--foil);
  }
  .front-mark .mark-name {
    font-size: 50px; font-weight: 700; color: var(--foil); letter-spacing: 2px;
  }
  .front-url {
    position: absolute; left: 0; right: 0; top: 200px;
    text-align: center; font-size: 13px; letter-spacing: 7px; color: var(--ink-muted);
  }

  /* back */
  .brand-block {
    position: absolute; left: 20px; top: 0; width: 265px; height: 100%;
    display: flex; flex-direction: column; align-items: center; justify-content: center;
  }
  .brand-name {
    font-size: 38px; font-weight: 700; color: var(--ink-white); letter-spacing: 1px;
  }
  .brand-tagline {
    margin-top: 10px; font-size: 13px; font-weight: 600; color: var(--ink-white);
    white-space: nowrap;
  }
  .divider {
    position: absolute; left: 300px; top: 55px; width: 1px; height: 190px;
    background: linear-gradient(to bottom, transparent, var(--ink-soft) 30%, var(--ink-soft) 70%, transparent);
  }
  .contact {
    position: absolute; left: 325px; top: 72px; color: var(--ink-white);
    font-size: 14px; line-height: 20px;
  }
  .contact .person-name { font-weight: 700; font-size: 15px; }
  .contact .person-role { margin-bottom: 6px; }
  .contact .line { display: flex; align-items: center; gap: 8px; }
  .contact svg { width: 12px; height: 12px; fill: var(--ink-white); flex: none; }
</style>
</head>
<body>
<div class="canvas">

  <section class="card card-front">
    <div class="front-mark">
      <span class="mark-square"></span>
      <span class="mark-name">KM&amp;DR</span>
    </div>
    <p class="front-url">www.kmanddr.com</p>
  </section>

  <section class="card card-back">
    <div class="brand-block">
      <span class="brand-name">KM&amp;DR</span>
      <span class="brand-tagline">Keystone Metal &amp; Drum Rolling</span>
    </div>
    <div class="divider"></div>
    <div class="contact">
      <p class="person-name">ALAN REYES</p>
      <p class="person-role">CEO/FOUNDER</p>
      <p>480 East 200 South</p>
      <p>Riverton Falls 84990</p>
      <p class="line">
        <svg viewBox="0 0 12 12" aria-hidden="true"><path d="M1 4 Q6 0 11 4 L9 5 L8 4 Q6 3 4 4 L3 5 Z M3 6 H9 L10 11 H2 Z"/></svg>
        555.310.4172
      </p>
      <p class="line">
        <svg viewBox="0 0 12 12" aria-hidden="true"><rect x="3" y="1" width="6" height="3"/><rect x="1" y="5" width="10" height="4" rx="1"/><rect x="3" y="9" width="6" height="2"/></svg>
        555.310.4190
      </p>
      <p class="line">
        <svg viewBox="0 0 12 12" aria-hidden="true"><circle cx="6" cy="6" r="5.5"/><path d="M1 6 H11 M6 .5 Q3 6 6 11.5 M6 .5 Q9 6 6 11.5" stroke="#141414" stroke-width="1" fill="none"/></svg>
        www.kmanddr.com
      </p>
    </div>
  </section>

</div>
</body>
</html>
```